New Business Card Design Project

We are looking for a talented individual to create a truly awesome/unique business card design for us. We are looking for a someone to design something that will really stand out from the crowd - we don't mind what ideas you come up with (ie embossed/flat/matte/shine etc etc) just wow us with your creativity.
Updates

Target Market(s)

Video Games Industry Professionals (all levels of seniority from QA Testers through to CEOs)

Contact Information for Business Card

Company logo (see upload)
Company name: Northbay Play Careers Ltd
Employee Name: Darren Elsby
Job title: CEO
Website: www.nbpc2go.example
Office +44 1632 960418
Mobile: +44 7700 900276
Email: darren@nbpc2go.example

Colors

Designer to choose colors to be used in the design.

Requirements
Must have
• The business card design MUST contain all the information listed in the BUSINESS CARD DETAILS box.
• You will see the colours that are relevant to us (ie company logo) in the uploaded imagery - however you do not have to use all these colours when designing the business card itself
• MUST BE DOUBLE SIDED

```html
<!DOCTYPE html>
<html lang="en">
<head>
<meta charset="utf-8">
<title>Northbay Play Careers – Business Card</title>
<link rel="stylesheet" href="https://fonts.googleapis.com/css2?family=Montserrat:wght@500;600;700;800&display=swap">
<style>
  :root {
    --stage: #161618;
    --card-back: #1e1f21;
    --card-front: #2a2b2e;
    --emboss: #111214;
    --emboss-edge: #34363a;
    --white: #ffffff;
    --orange: #f57c1f;
    --grey-text: #d9dadc;
    --navy: #2b3a78;
    --sky: #4a90d9;
  }
  * { margin: 0; padding: 0; box-sizing: border-box; }
  html, body { width: 1200px; height: 800px; overflow: hidden; }
  body {
    background: var(--stage);
    font-family: "Montserrat", sans-serif;
    position: relative;
  }
  .card {
    position: absolute;
    top: 250px;
    width: 525px;
    height: 300px;
    overflow: hidden;
    border-radius: 4px;
  }

  /* Back side */
  .card--back { left: 45px; background: var(--card-back); }
  .back-mark {
    position: absolute; left: 95px; top: 118px;
    display: flex; align-items: center; gap: 16px;
  }
  .back-mark__dot {
    width: 56px; height: 56px; border-radius: 50%;
    background: var(--emboss);
    box-shadow: 0 1px 0 var(--emboss-edge);
  }
  .back-mark__name {
    font-weight: 800; font-size: 27px; color: var(--emboss);
    text-shadow: 0 1px 0 var(--emboss-edge);
    letter-spacing: 0.3px;
  }

  /* Front side */
  .card--front { left: 630px; background: var(--card-front); }
  .front-watermark {
    position: absolute; right: -60px; top: -70px;
    width: 300px; height: 300px; border-radius: 50%;
    background: rgba(255,255,255,0.035);
  }
  .brand {
    position: absolute; left: 40px; top: 58px;
    display: flex; align-items: center; gap: 14px;
  }
  .brand__dot {
    width: 48px; height: 48px; border-radius: 50%;
    background: var(--navy);
  }
  .brand__name {
    font-weight: 800; font-size: 25px; color: var(--white);
    letter-spacing: 0.2px;
  }
  .social {
    position: absolute; right: 36px; top: 138px;
    display: flex; gap: 7px;
  }
  .social__box { width: 18px; height: 18px; border-radius: 2px; }
  .social__box--a { background: var(--navy); }
  .social__box--b { background: var(--sky); }
  .rule {
    position: absolute; left: 36px; right: 36px; top: 166px;
    height: 2px; background: var(--orange);
  }
  .person { position: absolute; left: 40px; top: 178px; }
  .person__name { font-weight: 700; font-size: 19px; color: var(--white); }
  .person__role { font-weight: 600; font-size: 13px; color: var(--orange); margin-top: 2px; }
  .rule--lower { top: 228px; left: 40px; right: 150px; height: 1.5px; }
  .contacts {
    position: absolute; left: 40px; top: 240px;
    display: flex; gap: 18px; align-items: stretch;
  }
  .contacts__group { display: flex; flex-direction: column; gap: 6px; }
  .contacts__divider { width: 1.5px; background: var(--orange); }
  .contact {
    display: flex; align-items: center; gap: 8px;
    font-weight: 500; font-size: 11.5px; color: var(--grey-text);
  }
  .contact--web { font-weight: 700; color: var(--white); }
  .contact__icon {
    width: 17px; height: 17px; border-radius: 50%;
    background: var(--orange);
    display: flex; align-items: center; justify-content: center;
    flex-shrink: 0;
  }
  .corner-tab {
    position: absolute; left: -22px; bottom: 18px;
    width: 44px; height: 44px; border-radius: 50%;
    background: var(--orange);
  }
</style>
</head>
<body>

<section class="card card--back" aria-label="Card back">
  <div class="back-mark">
    <span class="back-mark__dot"></span>
    <span class="back-mark__name">Northbay Play Careers</span>
  </div>
</section>

<section class="card card--front" aria-label="Card front">
  <div class="front-watermark"></div>
  <div class="brand">
    <span class="brand__dot"></span>
    <span class="brand__name">Northbay Play Careers</span>
  </div>
  <div class="social">
    <span class="social__box social__box--a"></span>
    <span class="social__box social__box--b"></span>
  </div>
  <div class="rule"></div>
  <div class="person">
    <div class="person__name">Darren Elsby</div>
    <div class="person__role">CEO</div>
  </div>
  <div class="rule rule--lower"></div>
  <div class="contacts">
    <div class="contacts__group">
      <div class="contact">
        <span class="contact__icon">
          <svg width="10" height="10" viewBox="0 0 10 10"><path d="M2 1h2l1 2-1.2 1a5 5 0 0 0 2.2 2.2L7 5l2 1v2c-4 0-8-4-8-8z" fill="#fff"/></svg>
        </span>
        +44 1632 960418
      </div>
      <div class="contact">
        <span class="contact__icon">
          <svg width="10" height="10" viewBox="0 0 10 10"><rect x="3" y="1" width="4.5" height="8" rx="0.8" fill="#fff"/><rect x="3.8" y="2" width="2.9" height="5" fill="#f57c1f"/></svg>
        </span>
        +44 7700 900276
      </div>
    </div>
    <span class="contacts__divider"></span>
    <div class="contacts__group">
      <div class="contact">
        <span class="contact__icon">
          <svg width="10" height="10" viewBox="0 0 10 10"><rect x="1" y="2.5" width="8" height="5.5" fill="#fff"/><path d="M1 2.5l4 3 4-3" stroke="#f57c1f" stroke-width="0.9" fill="none"/></svg>
        </span>
        darren@nbpc2go.example
      </div>
      <div class="contact contact--web">
        <span class="contact__icon">
          <svg width="10" height="10" viewBox="0 0 10 10"><circle cx="5" cy="5" r="3.8" fill="none" stroke="#fff" stroke-width="1"/><path d="M1.2 5h7.6M5 1.2c-2 2.5-2 5.1 0 7.6M5 1.2c2 2.5 2 5.1 0 7.6" stroke="#fff" stroke-width="0.8" fill="none"/></svg>
        </span>
        www.nbpc2go.example
      </div>
    </div>
  </div>
  <div class="corner-tab"></div>
</section>

</body>
</html>
```